Brightfield Optics seeks updated contemporary business card

Brightfield Optics utilizes advanced technology and we take pride in the modern look and feel of our practice. We like our current card, but it's been four years so it is time for an update.

Target Market(s)

Females 25-45 make the most health care decisions for their family.

Contact Information for Business Card

Clean front. Back with info and with empty space for appointment time or other small note

Requirements
Must have
• Logo
Ridge Marketvale, 28413 E Larkspur Ave
Cedar Terrace Marketvale, 4638 S Dunmore Rd
Call or text: 509-342-1968
email: hello@brightfieldoptics.example
brightfieldoptics.example
Dr Tobias Werring & Associates

```html
<!DOCTYPE html>
<html lang="en">
<head>
<meta charset="utf-8">
<title>Brightfield Optics – Business Card</title>
<link href="https://fonts.googleapis.com/css2?family=Source+Sans+3:wght@400;600;700&display=swap" rel="stylesheet">
<style>
  :root {
    --canvas: #e4e4e4;
    --card: #f4f4f4;
    --navy: #1f3e6b;
    --blue: #1a7ab0;
    --ink: #2c2c2c;
    --band-dark-start: #2a72a3;
    --band-dark-end: #173f66;
    --band-light-start: #2aa4dc;
    --band-light-end: #5cc2ea;
    --white: #ffffff;
  }
  * { margin: 0; padding: 0; box-sizing: border-box; }
  html, body { width: 1200px; height: 960px; overflow: hidden; }
  body {
    background: var(--canvas);
    font-family: "Source Sans 3", "Helvetica Neue", Arial, sans-serif;
    position: relative;
  }
  .card {
    position: absolute;
    left: 310px;
    width: 581px;
    height: 332px;
    background: var(--card);
    box-shadow: 2px 3px 6px rgba(0, 0, 0, 0.25);
  }
  .card--front { top: 127px; }
  .card--back { top: 509px; }

  .brand-name {
    position: absolute;
    font-weight: 700;
    color: var(--navy);
    letter-spacing: -0.3px;
    white-space: nowrap;
    line-height: 1;
  }
  .brand-tagline {
    position: absolute;
    font-weight: 700;
    color: var(--navy);
    font-size: 13px;
    letter-spacing: 0.2px;
    white-space: nowrap;
    line-height: 1;
  }
  .card--front .brand-name { left: 50px; top: 259px; font-size: 27px; }
  .card--front .brand-tagline { left: 95px; top: 287px; }

  .card--back .brand-name { left: 40px; top: 77px; font-size: 24px; }
  .card--back .brand-tagline { left: 80px; top: 112px; font-size: 12px; }

  .holder {
    position: absolute;
    right: 39px;
    top: 60px;
    text-align: right;
  }
  .holder__name { font-size: 19px; font-weight: 600; color: var(--blue); line-height: 1.2; }
  .holder__role { font-size: 15px; color: var(--ink); line-height: 1.2; }

  .practice {
    position: absolute;
    left: 39px;
    top: 167px;
    font-size: 15px;
    line-height: 19px;
    color: var(--ink);
  }
  .practice__associates { color: var(--blue); }

  .contact {
    position: absolute;
    left: 39px;
    top: 236px;
    font-size: 15px;
    line-height: 20px;
    color: var(--ink);
    list-style: none;
  }
  .contact__item { display: flex; align-items: center; gap: 4px; }
  .contact__icon { width: 13px; height: 13px; fill: var(--blue); flex: none; }

  .web-band {
    position: absolute;
    left: 0;
    top: 287px;
    width: 581px;
    height: 26px;
  }
  .web-band svg { position: absolute; inset: 0; }
  .web-band__url {
    position: absolute;
    right: 39px;
    top: 0;
    line-height: 26px;
    font-size: 15px;
    font-weight: 700;
    color: var(--white);
    white-space: nowrap;
  }
</style>
</head>
<body>

  <section class="card card--front" aria-label="Card front">
    <div class="brand-name">Brightfield Optics</div>
    <div class="brand-tagline">ADVANCED EYE CARE</div>
  </section>

  <section class="card card--back" aria-label="Card back">
    <div class="brand-name">Brightfield Optics</div>
    <div class="brand-tagline">ADVANCED EYE CARE</div>

    <div class="holder">
      <p class="holder__name">Daniel Hartley</p>
      <p class="holder__role">Founder</p>
    </div>

    <div class="practice">
      <p class="practice__associates">Dr Tobias Werring &amp; Associates</p>
      <p>Ridge Marketvale, 28413 E Larkspur Ave</p>
      <p>Cedar Terrace Marketvale, 4638 S Dunmore Rd</p>
    </div>

    <ul class="contact">
      <li class="contact__item">
        <svg class="contact__icon" viewBox="0 0 24 24" aria-hidden="true"><path d="M6.6 10.8a15.1 15.1 0 0 0 6.6 6.6l2.2-2.2c.3-.3.7-.4 1-.2 1.1.4 2.3.6 3.6.6.6 0 1 .4 1 1V20c0 .6-.4 1-1 1A17 17 0 0 1 3 4c0-.6.4-1 1-1h3.5c.6 0 1 .4 1 1 0 1.3.2 2.5.6 3.6.1.3 0 .7-.2 1z"/></svg>
        <span>509-342-1968</span>
      </li>
      <li class="contact__item">
        <svg class="contact__icon" viewBox="0 0 24 24" aria-hidden="true"><path d="M2 5h20v14H2zm2 2v.4l8 5 8-5V7zm0 2.8V17h16V9.8l-8 5z"/></svg>
        <span>hello@brightfieldoptics.example</span>
      </li>
    </ul>

    <div class="web-band">
      <svg width="581" height="26" viewBox="0 0 581 26" aria-hidden="true">
        <defs>
          <linearGradient id="bandDark" x1="0" x2="1">
            <stop offset="0" stop-color="var(--band-dark-start)"/>
            <stop offset="1" stop-color="var(--band-dark-end)"/>
          </linearGradient>
          <linearGradient id="bandLight" x1="0" x2="1">
            <stop offset="0" stop-color="var(--band-light-start)"/>
            <stop offset="1" stop-color="var(--band-light-end)"/>
          </linearGradient>
        </defs>
        <polygon points="0,0 340,0 348,13 340,26 0,26" fill="url(#bandDark)"/>
        <polygon points="344,0 581,0 581,26 344,26 352,13" fill="url(#bandLight)"/>
      </svg>
      <span class="web-band__url">brightfieldoptics.example</span>
    </div>
  </section>

</body>
</html>
```